New Business Card Design Project

I would like to purchase a customized version of a design you have previously submitted - https://www.plorvexa.com/design/7314826<br/><br/>I would like to incorporate the attached Images for my fitness company "TrelmoKor Athletics". My initial services is personal training and athletic performance. I would like a card that has one a shiny black side with the silver logo and the side with a white background utilizing the gold logo. On the white side, put "Sports Performance and Functional Strength Training" under the logo.
Industry/Entity Type
Fitness
Contact Information for Business Card
Quillan Morrow
Owner and Trainer
555.271.9384
quillan.morrow@trelmokorathletics.com
Look and feel
Each slider illustrates characteristics of the customer's brand and the style your logo design should communicate.

```html
<!DOCTYPE html>
<html lang="en">
<head>
<meta charset="utf-8">
<title>TrelmoKor Athletics — Business Card</title>
<link rel="stylesheet" href="https://fonts.googleapis.com/css2?family=Lato:wght@400;700&display=swap">
<style>
  :root {
    --backdrop: #e9ecec;
    --card-black: #121212;
    --card-edge: #1d1d1d;
    --card-white: #ffffff;
    --gold: #b8924a;
    --silver: #cfd2d4;
    --ink-light: #f2f2f2;
    --ink-muted: #c9c9c9;
    --ink-dark: #3a3a3a;
  }
  * { margin: 0; padding: 0; box-sizing: border-box; }
  html, body {
    width: 1200px;
    height: 900px;
    overflow: hidden;
    background: var(--backdrop);
    font-family: "Lato", sans-serif;
  }
  .canvas {
    width: 1200px;
    height: 900px;
    display: flex;
    flex-direction: column;
    align-items: center;
    justify-content: center;
    gap: 60px;
  }
  .card {
    position: relative;
    width: 560px;
    height: 320px;
    box-shadow: 0 14px 30px rgba(0, 0, 0, 0.18);
  }
  .brand-mark {
    display: flex;
    align-items: center;
    gap: 14px;
  }
  .brand-mark__circle {
    flex: none;
    border-radius: 50%;
  }
  .brand-mark__name {
    font-weight: 700;
    letter-spacing: 0.14em;
    text-transform: uppercase;
    line-height: 1.25;
  }

  /* Front face: white, gold mark centred with tagline */
  .card--front {
    background: var(--card-white);
    display: flex;
    flex-direction: column;
    align-items: center;
    justify-content: center;
    gap: 26px;
  }
  .card--front .brand-mark__circle {
    width: 74px;
    height: 74px;
    border: 3px solid var(--gold);
  }
  .card--front .brand-mark__name {
    color: var(--gold);
    font-size: 22px;
  }
  .tagline {
    font-size: 11px;
    font-weight: 400;
    letter-spacing: 0.12em;
    text-transform: uppercase;
    color: var(--ink-dark);
    text-align: center;
  }

  /* Back face: black, silver mark top right, contact bottom left */
  .card--back {
    background: linear-gradient(160deg, var(--card-edge), var(--card-black) 60%);
  }
  .card--back .brand-mark {
    position: absolute;
    right: 34px;
    top: 34px;
    gap: 10px;
  }
  .card--back .brand-mark__circle {
    width: 40px;
    height: 40px;
    border: 2px solid var(--silver);
  }
  .card--back .brand-mark__name {
    color: var(--silver);
    font-size: 13px;
  }
  .contact {
    position: absolute;
    left: 40px;
    bottom: 38px;
    color: var(--ink-light);
  }
  .contact__name {
    font-weight: 700;
    font-size: 30px;
    line-height: 1.1;
  }
  .contact__role {
    font-size: 13px;
    color: var(--ink-muted);
    margin-top: 4px;
  }
  .contact__phone {
    font-size: 28px;
    margin-top: 22px;
    letter-spacing: 0.02em;
  }
  .contact__email {
    font-size: 14px;
    margin-top: 6px;
    color: var(--ink-muted);
  }
</style>
</head>
<body>
  <main class="canvas">
    <section class="card card--front" aria-label="Card front">
      <div class="brand-mark">
        <span class="brand-mark__circle"></span>
        <span class="brand-mark__name">TrelmoKor<br>Athletics</span>
      </div>
      <p class="tagline">Sports Performance and Functional Strength Training</p>
    </section>

    <section class="card card--back" aria-label="Card back">
      <div class="brand-mark">
        <span class="brand-mark__circle"></span>
        <span class="brand-mark__name">TrelmoKor<br>Athletics</span>
      </div>
      <div class="contact">
        <p class="contact__name">Quillan Morrow</p>
        <p class="contact__role">Owner and Trainer</p>
        <p class="contact__phone">555.271.9384</p>
        <p class="contact__email">quillan.morrow@trelmokorathletics.com</p>
      </div>
    </section>
  </main>
</body>
</html>
```